Silver Birch Dental

I need a business card design for a state of the art and very modern dental practice. We provide general and pediatric dental services. I have attached a black and white EPS file of our logo, s logo design is not required. I have also attached two colors for our background and font. It does not have to be these two colors only. I am open to any suggestions. I have also included our current business card.
Things that should be different from our current business card is the logo, the website now is "www.silverbirchdental.com".
On the top right, where it says "like us on linkora", now should say "Download our app on tapshelf and zentro market store", but instead of our app, it should show the icon of our app, instead of tapshelf and zentro market, it should show their icons, and not spell the words out.
I have also attached what the front of the card should more or less look like. It is the one with the different size fonts. I need the icon for phone, email, address, etc next to each. It is the file name "back of the businesscard1".

Target Market(s)

18-35 year-olds

Industry/Entity Type

Dental

Requirements
Nice to have
• the icon of our app, melodrop, and zentro market on the top right.

```html
<!DOCTYPE html>
<html lang="en">
<head>
<meta charset="utf-8">
<title>Silver Birch Dental – Business Card</title>
<link rel="stylesheet" href="https://fonts.googleapis.com/css2?family=Lato:wght@300;400;700&display=swap">
<style>
  :root {
    --page-bg: #ffffff;
    --front-blue: #1a6e9e;
    --back-blue: #a9d5e8;
    --ink-blue: #1f6a99;
    --white: #ffffff;
  }
  * { margin: 0; padding: 0; box-sizing: border-box; }
  html, body { width: 900px; height: 1200px; overflow: hidden; background: var(--page-bg); }
  body { position: relative; font-family: "Lato", Arial, sans-serif; }

  .card {
    position: absolute;
    left: 21px;
    width: 858px;
    height: 462px;
    border-radius: 30px;
  }
  .card-front { top: 92px; background: var(--front-blue); display: flex; align-items: center; justify-content: center; }
  .card-back { top: 594px; background: var(--back-blue); color: var(--ink-blue); }

  .holder-name { color: var(--white); font-size: 40px; font-weight: 400; letter-spacing: 1px; }
  .holder-name .credential { font-weight: 300; }

  .download-row {
    position: absolute; top: 42px; right: 50px;
    display: flex; align-items: center; gap: 10px;
    font-size: 10px; font-weight: 700; letter-spacing: 1px;
  }
  .app-icon { width: 44px; height: 44px; border-radius: 8px; background: var(--ink-blue); }
  .store-icon-round { width: 44px; height: 44px; border-radius: 50%; background: #6f86c9; }
  .store-icon-square { width: 40px; height: 40px; border-radius: 4px; background: #e0923a; }

  .practice-mark {
    position: absolute; left: 190px; top: 42px;
    width: 86px; height: 86px; border-radius: 50%;
    border: 4px solid var(--ink-blue);
  }
  .practice-name {
    position: absolute; left: 190px; top: 146px;
    font-size: 46px; font-weight: 300; letter-spacing: 2px; text-transform: uppercase;
    white-space: nowrap;
  }

  .contact-list { position: absolute; left: 226px; top: 240px; list-style: none; }
  .contact-item { display: flex; align-items: center; gap: 12px; white-space: nowrap; }
  .contact-item svg { flex: none; fill: var(--ink-blue); }
  .contact-address { font-size: 21px; height: 38px; }
  .contact-phone { font-size: 54px; font-weight: 300; height: 66px; }
  .contact-email { font-size: 21px; height: 40px; }
  .contact-web { font-size: 44px; font-weight: 300; height: 56px; }
</style>
</head>
<body>
  <section class="card card-front">
    <h1 class="holder-name">DANIEL REYES <span class="credential">DDS</span></h1>
  </section>

  <section class="card card-back">
    <div class="download-row">
      <span>DOWNLOAD</span>
      <span class="app-icon" role="img" aria-label="Silver Birch Dental app icon"></span>
      <span>ON</span>
      <span class="store-icon-round" role="img" aria-label="tapshelf store icon"></span>
      <span>&amp;</span>
      <span class="store-icon-square" role="img" aria-label="zentro market store icon"></span>
    </div>

    <span class="practice-mark" aria-hidden="true"></span>
    <div class="practice-name">Silver Birch Dental</div>

    <ul class="contact-list">
      <li class="contact-item contact-address">
        <svg width="18" height="24" viewBox="0 0 20 26" aria-hidden="true"><path d="M10 0C4.5 0 0 4.4 0 9.8 0 17 10 26 10 26s10-9 10-16.2C20 4.4 15.5 0 10 0zm0 13.5a3.7 3.7 0 1 1 0-7.4 3.7 3.7 0 0 1 0 7.4z"/></svg>
        <span>412 Maple Row, Brookfield, NY, 11020</span>
      </li>
      <li class="contact-item contact-phone">
        <svg width="24" height="20" viewBox="0 0 26 22" aria-hidden="true"><path d="M13 4C7 4 1.5 5.5 0 8.5L2.5 12 7 10.5V7.5c2-.8 10-.8 12 0v3l4.5 1.5L26 8.5C24.5 5.5 19 4 13 4zM6 14h14l2 6H4z"/></svg>
        <span>(555) 014-2290</span>
      </li>
      <li class="contact-item contact-email">
        <svg width="22" height="16" viewBox="0 0 24 18" aria-hidden="true"><path d="M0 0h24v18H0zM2 2.5v.6l10 7 10-7v-.6zM2 5.5V16h20V5.5l-10 7z"/></svg>
        <span>hello@silverbirchdental.com</span>
      </li>
      <li class="contact-item contact-web">
        <svg width="22" height="22" viewBox="0 0 24 24" aria-hidden="true"><path d="M12 0a12 12 0 1 0 0 24 12 12 0 0 0 0-24zm7.9 7h-3.4a18 18 0 0 0-1.6-4.4A9.6 9.6 0 0 1 19.9 7zM12 2.4c.9 1.3 1.7 2.8 2.1 4.6H9.9c.4-1.8 1.2-3.3 2.1-4.6zM2.7 14a9.6 9.6 0 0 1 0-4h3.9a20 20 0 0 0 0 4zm1.4 3h3.4c.4 1.6.9 3.1 1.6 4.4A9.6 9.6 0 0 1 4.1 17zM7.5 7H4.1a9.6 9.6 0 0 1 5-4.4A18 18 0 0 0 7.5 7zM12 21.6c-.9-1.3-1.7-2.8-2.1-4.6h4.2c-.4 1.8-1.2 3.3-2.1 4.6zM14.6 14H9.4a17 17 0 0 1 0-4h5.2a17 17 0 0 1 0 4zm.3 7.4c.7-1.3 1.2-2.8 1.6-4.4h3.4a9.6 9.6 0 0 1-5 4.4zM17.4 14a20 20 0 0 0 0-4h3.9a9.6 9.6 0 0 1 0 4z"/></svg>
        <span>www.silverbirchdental.com</span>
      </li>
    </ul>
  </section>
</body>
</html>
```